8x8 Social Media Ad - Harbor Summit Expo

Attention Real Estate Agents
Please join us for our
Quarterly Real Estate Training Expo
The 2nd Saturday of February, May, August and November
Our Next Training Expo is _________________________________
From 9 am to 1 pm
at
Marlowe Suites Fernridge Station
4187 Copperleaf Lane, Greenbelt, MD 20770
Scheduled Speakers
9:00 am - Desmond Pryce - Orientation
9:30 am - Terrell Oakes - Multiple Income Streams / Keystone Track
10:00 am - Lorna Beckett - Marketing though Social Media
10:45 am - Raul Denning - Generating Business through Kelp-Nest
11:30 am - Tunde Adesemi - Real Estate Investing
12:15 pm - Marcus Oyelowo - (Main Speaker) Training Topic TBA
For more information call Desmond Pryce at (240) 555-0192 or email dpryce@harborsummithomes.example

```html
<!DOCTYPE html>
<html lang="en">
<head>
<meta charset="utf-8">
<title>Harbor Summit Expo – Quarterly Real Estate Training Expo</title>
<link href="https://fonts.googleapis.com/css2?family=Anton&family=Poppins:wght@300;400;500;600;700&display=swap" rel="stylesheet">
<style>
  :root {
    --teal: #17929b;
    --teal-bright: #1aa3ad;
    --ink: #1f1e20;
    --paper: #ffffff;
  }
  * { margin: 0; padding: 0; box-sizing: border-box; }
  html, body { width: 1200px; height: 1200px; overflow: hidden; background: var(--paper); }
  .ad {
    position: relative; width: 1200px; height: 1200px; overflow: hidden;
    background: var(--paper); font-family: 'Poppins', sans-serif; color: var(--ink);
  }
  .hero-art { position: absolute; left: 0; top: 0; }
  .brand {
    position: absolute; left: 26px; top: 78px; width: 190px;
    display: flex; align-items: center; gap: 10px; z-index: 2;
  }
  .brand-mark { width: 22px; height: 22px; background: var(--teal); flex: none; }
  .brand-name {
    font-family: 'Poppins', sans-serif; font-weight: 600; font-size: 22px;
    line-height: 1.15; color: var(--teal); text-transform: uppercase;
  }
  .invite {
    position: absolute; left: 630px; top: 26px; z-index: 2;
    font-weight: 400; font-size: 31px; color: var(--paper); letter-spacing: 0.5px;
  }
  .details { position: absolute; left: 208px; top: 587px; width: 783px; height: 130px; display: flex; }
  .details-when { width: 388px; background: var(--ink); color: var(--paper); padding: 8px 0 0 14px; }
  .details-when .day { font-size: 35px; font-weight: 500; line-height: 1.2; }
  .details-when .months { font-size: 18px; margin: 2px 0 0 4px; }
  .details-when .months-highlight { font-size: 27px; font-weight: 500; color: var(--teal-bright); margin: 4px 0 0 4px; line-height: 1.1; }
  .details-where { flex: 1; background: var(--teal); color: var(--paper); padding: 4px 0 0 27px; }
  .details-where .hours { font-size: 35px; font-weight: 500; line-height: 1.2; }
  .details-where .venue { font-size: 17.5px; font-weight: 500; line-height: 1.45; margin-top: 2px; }
  .next-date { position: absolute; left: 208px; top: 746px; font-size: 20px; font-weight: 500; }
  .speakers-band { position: absolute; left: 0; top: 794px; width: 1200px; height: 336px; background: var(--teal); }
  .speakers-title {
    position: absolute; left: 0; top: 15px; width: 1220px; text-align: center;
    font-weight: 700; font-size: 27px; color: var(--paper); letter-spacing: 0.5px;
  }
  .speaker { position: absolute; top: 80px; width: 196px; text-align: center; color: var(--paper); }
  .speaker-photo {
    display: block; width: 76px; height: 76px; margin: 0 auto; border-radius: 50%;
    border: 2px solid var(--paper);
    background: radial-gradient(circle at 50% 40%, #6b5a50 0%, #3a3230 55%, #1e1b1b 100%);
  }
  .speaker-name { font-size: 17px; font-weight: 500; margin-top: 10px; line-height: 1.3; white-space: nowrap; }
  .speaker-topic { font-size: 13.5px; line-height: 1.4; height: 40px; }
  .speaker-time { font-family: 'Anton', sans-serif; font-size: 25px; line-height: 1.3; margin-top: 2px; }
  .divider { position: absolute; top: 87px; width: 1px; height: 177px; background: rgba(255,255,255,0.85); }
  .more-info {
    position: absolute; left: 0; top: 284px; width: 1216px; text-align: center;
    font-weight: 700; font-size: 17px; color: var(--ink);
  }
  .contact-bar {
    position: absolute; left: 102px; top: 1112px; width: 1015px; height: 38px;
    background: var(--ink); color: var(--paper); font-size: 19px; font-weight: 500;
    display: flex; align-items: center; justify-content: center; white-space: nowrap;
  }
</style>
</head>
<body>
<main class="ad">
  <svg class="hero-art" width="1200" height="580" viewBox="0 0 1200 580">
    <defs>
      <linearGradient id="skylineTone" x1="0" y1="0" x2="0" y2="1">
        <stop offset="0" stop-color="#17929b"/>
        <stop offset="0.55" stop-color="#146f76"/>
        <stop offset="1" stop-color="#111"/>
      </linearGradient>
    </defs>
    <polygon class="hero-band" points="413,0 1200,0 1012,305 208,340" fill="#1f1e20"/>
    <polygon class="skyline" points="208,340 208,300 232,290 335,125 528,59 580,59 640,105 790,100 860,120 1000,180 1012,300 1012,340"
             fill="url(#skylineTone)" role="img" aria-label="City skyline silhouette with teal and black towers and a Ferris wheel"/>
    <text x="208" y="500" textLength="808" lengthAdjust="spacingAndGlyphs"
          font-family="Anton, sans-serif" font-size="218" fill="#1f1e20"
          stroke="#ffffff" stroke-width="5" paint-order="stroke">QUARTERLY</text>
    <text x="208" y="567" textLength="798" lengthAdjust="spacingAndGlyphs"
          font-family="Poppins, sans-serif" font-weight="500" font-size="61" fill="#1f1e20">REAL ESTATE TRAINING EXPO</text>
  </svg>

  <div class="brand">
    <span class="brand-mark"></span>
    <span class="brand-name">Harbor Summit<br>Realty Group</span>
  </div>

  <p class="invite">PLEASE JOIN US FOR OUR</p>

  <section class="details">
    <div class="details-when">
      <p class="day">THE 2ND SATURDAY</p>
      <p class="months">of February, May,</p>
      <p class="months-highlight">AUGUST &amp; NOVEMBER</p>
    </div>
    <div class="details-where">
      <p class="hours">FROM 9 AM TO 1 PM</p>
      <p class="venue">at Marlowe Suites Fernridge Station<br>4187 Copperleaf Lane,<br>Greenbelt, MD 20770</p>
    </div>
  </section>

  <p class="next-date">Our Next Training Expo is ______________________________________</p>

  <section class="speakers-band">
    <h2 class="speakers-title">SCHEDULED SPEAKERS</h2>

    <div class="speaker" style="left:18px">
      <span class="speaker-photo" role="img" aria-label="Portrait photo of Desmond Pryce"></span>
      <p class="speaker-name">DESMOND PRYCE</p>
      <p class="speaker-topic">Orientation</p>
      <p class="speaker-time">9:00 AM</p>
    </div>
    <span class="divider" style="left:209px"></span>
    <div class="speaker" style="left:206px">
      <span class="speaker-photo" role="img" aria-label="Portrait photo of Terrell Oakes"></span>
      <p class="speaker-name">TERRELL OAKES</p>
      <p class="speaker-topic">Multiple Income<br>Streams / Keystone Track</p>
      <p class="speaker-time">9:30 AM</p>
    </div>
    <span class="divider" style="left:404px"></span>
    <div class="speaker" style="left:407px">
      <span class="speaker-photo" role="img" aria-label="Portrait photo of Lorna Beckett"></span>
      <p class="speaker-name">LORNA BECKETT</p>
      <p class="speaker-topic">Marketing though<br>Social Media</p>
      <p class="speaker-time">10:00 AM</p>
    </div>
    <span class="divider" style="left:600px"></span>
    <div class="speaker" style="left:602px">
      <span class="speaker-photo" role="img" aria-label="Portrait photo of Raul Denning"></span>
      <p class="speaker-name">RAUL DENNING</p>
      <p class="speaker-topic">Generating Business<br>through Kelp-Nest</p>
      <p class="speaker-time">10:45 AM</p>
    </div>
    <span class="divider" style="left:795px"></span>
    <div class="speaker" style="left:801px">
      <span class="speaker-photo" role="img" aria-label="Portrait photo of Tunde Adesemi"></span>
      <p class="speaker-name">TUNDE ADESEMI</p>
      <p class="speaker-topic">Real Estate<br>Investing</p>
      <p class="speaker-time">11:30AM</p>
    </div>
    <span class="divider" style="left:991px"></span>
    <div class="speaker" style="left:992px">
      <span class="speaker-photo" role="img" aria-label="Portrait photo of Marcus Oyelowo"></span>
      <p class="speaker-name">MARCUS OYELOWO</p>
      <p class="speaker-topic">(Main Speaker)<br>Training Topic TBA</p>
      <p class="speaker-time">12:15 PM</p>
    </div>

    <p class="more-info">FOR MORE INFORMATION</p>
  </section>

  <p class="contact-bar">CALL DESMOND PRYCE AT (240) 555-0192 OR EMAIL DPRYCE@HARBORSUMMITHOMES.EXAMPLE</p>
</main>
</body>
</html>
```